Home Security Company Business Card

Looking for a eye catching business card that is non traditional and stands out but yet still looks professional. It should include all the pertinent information such as name, title, address, telephone, e-mail, website address should definitely stand out and then finally the logo.

Target Market(s)

Residential and Commercial accounts mostly upscale accounts

Industry/Entity Type

Security

Contact Information for Business Card

Name
Title
Address
Office #
Cell #
E-mail
Website

Font styles to use
Serif
Sans Serif

Requirements
Must have
• Logo, two sided color configuration
Nice to have
• You decide
Should not have
• There really aren't any.

```html
<!DOCTYPE html>
<html lang="en">
<head>
<meta charset="utf-8">
<title>Wardenly Security Systems – Business Card</title>
<link rel="stylesheet" href="https://fonts.googleapis.com/css2?family=Crimson+Pro:wght@400;600;700&display=swap">
<style>
  :root {
    --maroon: #7a1416;
    --gold: #e6b548;
    --white: #ffffff;
    --backdrop: #efe9df;
  }
  * { margin: 0; padding: 0; box-sizing: border-box; }
  html, body { width: 1189px; height: 1200px; overflow: hidden; }
  body {
    background: var(--backdrop);
    font-family: "Crimson Pro", Georgia, serif;
    position: relative;
  }
  .card {
    position: absolute;
    left: 171px;
    width: 856px;
    height: 488px;
    border-radius: 20px;
    background: var(--white);
    overflow: hidden;
  }
  .card--front { top: 67px; }
  .card--back { top: 627px; }
  .card__shapes { position: absolute; inset: 0; }

  .brand-mark {
    position: absolute;
    background: var(--gold);
  }
  .brand-name {
    position: absolute;
    color: var(--maroon);
    font-weight: 400;
    line-height: 1.15;
  }
  .card--front .brand-mark { left: 120px; top: 198px; width: 92px; height: 92px; }
  .card--front .brand-name { left: 240px; top: 221px; font-size: 40px; white-space: nowrap; }

  .card--back .brand-mark { left: 601px; top: 100px; width: 100px; height: 100px; }
  .card--back .brand-name { left: 471px; top: 250px; width: 360px; font-size: 34px; text-align: center; }

  .contact { position: absolute; color: var(--white); line-height: 1; white-space: nowrap; }
  .contact__name { left: 34px; top: 84px; font-size: 36px; font-weight: 700; }
  .contact__title { left: 34px; top: 118px; font-size: 21px; letter-spacing: 1px; }
  .contact__address { left: 34px; top: 183px; font-size: 24px; letter-spacing: 0.5px; line-height: 30px; }
  .contact__row { left: 34px; font-size: 24px; letter-spacing: 0.5px; display: flex; align-items: center; gap: 15px; }
  .contact__row svg { width: 20px; height: 20px; flex: none; }
  .contact__row--office { top: 260px; }
  .contact__row--cell { top: 290px; }
  .contact__row--email { top: 319px; }
  .contact__web { left: 34px; top: 375px; font-size: 24px; letter-spacing: 1px; }
</style>
</head>
<body>

<section class="card card--front" aria-label="Card front">
  <span class="brand-mark"></span>
  <span class="brand-name">Wardenly Security Systems Inc.</span>
</section>

<section class="card card--back" aria-label="Card back">
  <svg class="card__shapes" viewBox="0 0 856 488" aria-hidden="true">
    <path d="M0,0 H432 C360,160 360,330 431,488 H0 Z" fill="var(--maroon)"/>
    <path d="M434,0 C366,160 366,330 433,488 L436,488 C376,330 376,160 438,0 Z" fill="var(--gold)"/>
  </svg>

  <div class="contact contact__name">Marla Quintero</div>
  <div class="contact contact__title">Managing Director</div>
  <div class="contact contact__address">PO Box 418 Kestrel Way<br>Brookfield, USA</div>

  <div class="contact contact__row contact__row--office">
    <svg viewBox="0 0 20 20" aria-hidden="true"><rect x="0" y="0" width="20" height="20" rx="3" fill="var(--white)"/><path d="M4,8 C4,5 16,5 16,8 L14,9 L13,7 H7 L6,9 Z M6,10 H14 L15,15 H5 Z" fill="var(--maroon)"/><circle cx="10" cy="12.5" r="1.6" fill="var(--white)"/></svg>
    <span>555-284-1937</span>
  </div>
  <div class="contact contact__row contact__row--cell">
    <svg viewBox="0 0 20 20" aria-hidden="true"><rect x="0" y="0" width="20" height="20" rx="3" fill="var(--white)"/><rect x="6" y="3" width="8" height="14" rx="1.5" fill="var(--maroon)"/><rect x="7.5" y="5" width="5" height="4" fill="var(--white)"/><rect x="7.5" y="10.5" width="5" height="5" fill="var(--white)" opacity="0.7"/></svg>
    <span>+1 555-284-1937</span>
  </div>
  <div class="contact contact__row contact__row--email">
    <svg viewBox="0 0 20 20" aria-hidden="true"><rect x="0" y="0" width="20" height="20" rx="3" fill="var(--white)"/><rect x="3" y="5" width="14" height="10" fill="none" stroke="var(--maroon)" stroke-width="1.4"/><path d="M3,5 L10,11 L17,5 M3,15 L8,9.5 M17,15 L12,9.5" fill="none" stroke="var(--maroon)" stroke-width="1.2"/></svg>
    <span>info@wardenlyss.com</span>
  </div>
  <div class="contact contact__web">www.wardenlyss.com</div>

  <span class="brand-mark"></span>
  <span class="brand-name">Wardenly Security Systems Inc.</span>
</section>

</body>
</html>
```